Request for Business Card Design

Hi. My name is Marlena, I am looking for a new business card design for my company, Quillbrook Sensing Systems, LLC. I really like the design you did for Tavel Harvest and was hoping you could do something similar using our full logo and our mark. I am also open to any raised texture design using our mark. I have attached our full logo, which would need to be somewhere on the card, as well as the mark in both outline and full form, as well as our brand colors / guide. The card does not have to be white, as long as our logo and mark appear. I actually like darker colored business cards more, but am open to all options. If you are interested in working with me, please let me know. We would also take the business card design into letterhead design if you can do that.

```html
<!DOCTYPE html>
<html lang="en">
<head>
<meta charset="utf-8">
<title>Quillbrook Sensing Systems — Business Card</title>
<link rel="stylesheet" href="https://fonts.googleapis.com/css2?family=Barlow:wght@500;600;700&display=swap">
<style>
  :root {
    --stage: #77777b;
    --stage-dark: #5a5a5e;
    --paper: #ffffff;
    --ink: #3a3a3c;
    --brand-blue: #0a9bc4;
    --card-dark: #3b3b3d;
    --emboss: #333335;
  }
  * { box-sizing: border-box; margin: 0; padding: 0; }
  html, body { width: 1200px; height: 876px; overflow: hidden; }
  body {
    background: radial-gradient(ellipse at 50% 35%, var(--stage) 0%, var(--stage-dark) 100%);
    font-family: "Barlow", Arial, sans-serif;
    position: relative;
  }
  .card {
    position: absolute;
    top: 290px;
    width: 520px;
    height: 297px;
    border-radius: 3px;
    box-shadow: 0 14px 30px rgba(0,0,0,0.35);
    overflow: hidden;
  }
  .card--front { left: 50px; background: var(--paper); color: var(--ink); }
  .card--back { left: 630px; background: var(--card-dark); }

  .wordmark {
    display: flex; align-items: center; gap: 12px;
  }
  .wordmark__dot { width: 30px; height: 30px; border-radius: 50%; background: var(--brand-blue); flex: none; }
  .wordmark__name {
    font-weight: 700; text-transform: uppercase; line-height: 1.05;
    letter-spacing: 0.04em;
  }
  .card--front .wordmark { position: absolute; left: 30px; top: 26px; }
  .card--front .wordmark__name { font-size: 20px; color: var(--ink); }

  .person { position: absolute; left: 30px; top: 100px; }
  .person__name { font-size: 20px; font-weight: 600; color: var(--brand-blue); text-transform: uppercase; letter-spacing: 0.02em; }
  .person__title { font-size: 12px; font-weight: 500; margin-top: 2px; }

  .contact { position: absolute; left: 30px; top: 160px; list-style: none; font-size: 12px; font-weight: 500; letter-spacing: 0.04em; }
  .contact li { display: flex; align-items: center; gap: 7px; height: 19px; }
  .contact svg { width: 10px; height: 10px; fill: var(--brand-blue); flex: none; }

  .mark-area {
    position: absolute; right: 40px; top: 60px;
    width: 170px; height: 170px; border-radius: 50%;
    background: var(--brand-blue);
  }
  .address {
    position: absolute; right: 30px; bottom: 20px; text-align: right;
    font-size: 12px; font-weight: 500; letter-spacing: 0.04em; line-height: 1.5;
  }

  .card--back .wordmark { position: absolute; left: 50%; top: 50%; transform: translate(-50%, -50%); gap: 16px; }
  .card--back .wordmark__dot { width: 40px; height: 40px; }
  .card--back .wordmark__name {
    font-size: 28px; color: var(--emboss);
  }
</style>
</head>
<body>
  <section class="card card--front" aria-label="Business card front">
    <div class="wordmark">
      <span class="wordmark__dot"></span>
      <span class="wordmark__name">Quillbrook<br>Sensing Systems</span>
    </div>

    <div class="person">
      <p class="person__name">Nolan Reyes</p>
      <p class="person__title">President</p>
    </div>

    <ul class="contact">
      <li><svg viewBox="0 0 10 10"><path d="M2 0.5 L3.6 2.6 L2.7 3.6 Q3.6 5.8 6.4 7.3 L7.4 6.4 L9.5 8 L8.3 9.5 Q1 7.5 0.5 1.7 Z"/></svg>555 210 4837</li>
      <li><svg viewBox="0 0 10 10"><rect x="1" y="3" width="8" height="6" rx="1"/><rect x="2.5" y="0.5" width="5" height="3"/></svg>555 210 4890</li>
      <li><svg viewBox="0 0 10 10"><path d="M0.5 2 H9.5 V8.5 H0.5 Z M1.2 2.6 L5 5.6 L8.8 2.6" stroke="#fff" stroke-width="0.8"/></svg>info@quillbrooksensing.com</li>
      <li><svg viewBox="0 0 10 10"><circle cx="5" cy="5" r="4.5"/><path d="M0.5 5 H9.5 M5 0.5 V9.5" stroke="#fff" stroke-width="0.8"/></svg>www.quillbrooksensing.com</li>
    </ul>

    <div class="mark-area" role="img" aria-label="Large brand mark area"></div>

    <p class="address">1180 Ridgeline Parkway<br>Alder Falls, CO 80977</p>
  </section>

  <section class="card card--back" aria-label="Business card back">
    <div class="wordmark">
      <span class="wordmark__dot"></span>
      <span class="wordmark__name">Quillbrook<br>Sensing Systems</span>
    </div>
  </section>
</body>
</html>
```